Crime/mystery/thriller novel cover design

I am looking to get a cover designed for a novel. It is a crime/mystery/thriller set in Liverpool, England, between the 1970s and current day. I have permission to use some paintings by an artist for the cover, so it just needs put together and jazzed up. I am looking for something which has a fairly classic feel (so not just pulp airport thriller trash) but with some flair nonetheless.
The novel will be paperback, 127mm x 203mm with approx 18mm spine width. Can be gloss or matt cover, would be interesting to discuss.
The title is:
THE HARBOUR LANTERN
Author name:
GORDON T. VESELKA
Publisher:
BRIVOLTA PUBLISHING LTD (or simply BRIVOLTA)

I am still working on the back cover blurb but I will upload this when finished.
There are 4 images I could use for the cover though my favourite is the one called Dusk, Quayside Terraces.

```html
<!DOCTYPE html>
<html lang="en">
<head>
<meta charset="utf-8">
<title>The Harbour Lantern – Cover</title>
<link rel="stylesheet" href="https://fonts.googleapis.com/css2?family=Cabin:ital,wght@0,400;0,500;1,400&display=swap">
<style>
  :root {
    --back-bg: #3d3e3b;
    --title-white: #f4f4f0;
    --body-text: #ecece8;
    --author-yellow: #f2e35c;
    --imprint-grey: #8d8d88;
    --sky-dark: #2c302c;
    --sky-mid: #4c5442;
    --glow-yellow: #e7d64a;
    --glow-pale: #f2e98a;
    --silhouette: #2f302d;
    --reflect-orange: #c9853c;
  }
  * { margin: 0; padding: 0; box-sizing: border-box; }
  html, body { width: 1200px; height: 892px; overflow: hidden; background: var(--back-bg); }
  body { font-family: "Cabin", "Gill Sans", sans-serif; }

  .jacket { position: relative; width: 1200px; height: 892px; }

  /* Back cover */
  .back-cover { position: absolute; left: 0; top: 0; width: 551px; height: 892px; background: var(--back-bg); }
  .back-title {
    position: absolute; left: 0; top: 98px; width: 560px; text-align: center;
    color: var(--title-white); font-weight: 400; font-size: 31px; letter-spacing: 0.62em; line-height: 46px;
  }
  .blurb { position: absolute; left: 65px; top: 218px; width: 440px; color: var(--body-text); font-size: 13.2px; letter-spacing: 0.05em; line-height: 18px; }
  .blurb p { margin-bottom: 15px; }
  .review { position: absolute; left: 62px; top: 530px; color: var(--body-text); font-size: 11.8px; letter-spacing: 0.03em; line-height: 20px; }
  .review q { font-style: italic; quotes: "\"" "\""; }

  .imprint-name { position: absolute; text-align: center; color: var(--imprint-grey); font-weight: 500; letter-spacing: 0.08em; }
  .imprint--back { left: 222px; top: 666px; width: 120px; font-size: 15px; }
  .imprint--spine { left: 568px; top: 65px; width: 60px; font-size: 8px; letter-spacing: 0.04em; }

  /* Spine + front painting */
  .cover-art {
    position: absolute; left: 551px; top: 0; width: 649px; height: 892px;
    background:
      linear-gradient(180deg,
        var(--sky-dark) 0%, var(--sky-mid) 22%, #5d6340 36%,
        var(--glow-yellow) 46%, var(--glow-pale) 51%, var(--glow-yellow) 55%,
        var(--silhouette) 60%, var(--silhouette) 76%,
        var(--reflect-orange) 84%, #8a6438 92%, #3a3630 100%);
  }
  .spine-shade { position: absolute; left: 551px; top: 0; width: 96px; height: 892px; background: linear-gradient(90deg, rgba(30,30,28,0.55), rgba(30,30,28,0)); }

  .spine-text {
    position: absolute; left: 586px; writing-mode: vertical-rl;
    font-size: 24px; letter-spacing: 0.38em; line-height: 1; white-space: nowrap;
  }
  .spine-title { top: 103px; color: var(--title-white); }
  .spine-author { top: 551px; color: var(--author-yellow); font-size: 22px; letter-spacing: 0.255em; }

  .front-author {
    position: absolute; left: 655px; top: 104px; width: 545px; text-align: center;
    color: var(--author-yellow); font-size: 27px; font-weight: 500; letter-spacing: 0.36em;
  }
  .front-title {
    position: absolute; left: 650px; top: 186px; width: 550px; text-align: center;
    color: var(--title-white); font-weight: 400; font-size: 35px; letter-spacing: 0.6em; line-height: 49px;
  }
</style>
</head>
<body>
<div class="jacket">
  <section class="back-cover">
    <h2 class="back-title">THE HARBOUR<br>LANTERN</h2>
    <div class="blurb">
      <p>London at the turn of the millennium and Christopher Kingstone QC has enough on his plate with a broken down marriage, unruly daughter and backstabbing colleagues.</p>
      <p>Just when things might be starting to look up, an unexpected package arrives bearing his late uncle's dying wish. Before long he finds himself reluctantly returning to his native Liverpool to undertake a seemingly hopeless task - to finally uncover the truth behind the violent murder of his beloved cousin April back when they were teenagers in Crosby in the 1970s.</p>
      <p>But as he digs ever deeper into the murky waters of the past, skeletons begin to tumble from closets and as things spiral rapidly out of control he discovers all too late that sometimes the past should remain firmly in the past.</p>
    </div>
    <div class="review">
      <q>Beautifully written, intelligently constructed and with just the correct amount of humour</q><br>
      - Helen Marlowe, Crime Author
    </div>
    <div class="imprint-name imprint--back">BRIVOLTA</div>
  </section>

  <div class="cover-art" role="img" aria-label="Painting: Dusk, Quayside Terraces – dark waterfront buildings silhouetted against a glowing yellow sky, reflected in the river"></div>
  <div class="spine-shade"></div>

  <div class="imprint-name imprint--spine">BRIVOLTA</div>
  <div class="spine-text spine-title">THE HARBOUR LANTERN</div>
  <div class="spine-text spine-author">GORDON T. VESELKA</div>

  <div class="front-author">GORDON T. VESELKA</div>
  <h1 class="front-title">THE HARBOUR<br>LANTERN</h1>
</div>
</body>
</html>
```